Facilities & Property Consultant Business Card

I am a building services and facilities professional who has worked for 18 years. I am now ready to start working for myself providing the same service on a consultancy basis. I have set up the company and its called KVT 3, the 2 is used as in squared, as in the area of a building 120,000 metres squared!- Hope that makes sense.
I am looking for initially a business card design but will want a website theme to be created as well.
The A in the company name is my surname, my work often involves project management of building work or facility projects so the P and the M is both property and project related. And then the m2 can be looked upon as the unit of area metres squared.
i am looking for a clean and sophisticated logo, nothing childlike or too playful. I want it to look stylish. I am a big fan of less is more and don't expect fussy or busy designs

I have no preferences for colour. Phone no for card will be 07945 318264
It should have my domain address which is www.kvt3.co and my email address which is daniel@kvt3.co. The 2 should be set higher than the m so it looks like it would if it was written mathematically.

I would like a QR code on the card with my details as well so please allow for that . I want it to be a code that has my details to be added to an address book as a contact

My selling point for this business is me!, my years of experience, my safe pair of hands in getting the job done with no fuss or drama. I will also provide safety advice and guidance as I chartered in safety, or very shortly will be. But my main thrust will be on interim projects with organisations that need experience for short periods or on retainer for a few days per month.
I will also have a network of building related , capable professionals that I can rely on in other disciplines of the property industry.

.
Updates

Can you all please revisit the brief and ensure you include the contact details i have provided on to the design. 

Also the QR code as well.

Regards
Dan Kessop 

Reason: I will be away for 7 days from 8th June on leave and I am very close on some of the submissions but think that a bit more time will provide some more variety in the submissions. Thankyou so much so far . Dan Kessop

Reason: Just back from a trip abroad, just a few more days to see if the next submitted design is the one that jumps out of the page. Thanks to all of you who have submitted so far.

Industry/Entity Type

Building

Requirements
Must have
• My contact details that are in the brief above, the Qr code on one side with my contact information, the reverse Side of the card should have my logo/design and only my phone number.

Image size for printing 1039 x 697 pixels 300 dpi

```html
<!DOCTYPE html>
<html lang="en">
<head>
<meta charset="utf-8">
<title>KVT 3 — Business Card Reverse</title>
<link rel="stylesheet" href="https://fonts.googleapis.com/css2?family=Varela+Round&display=swap">
<style>
  :root {
    --page: #ffffff;
    --card: #ffffff;
    --card-edge: #2b2b2b;
    --brand-blue: #00a0e0;
    --brand-red: #e31e26;
    --text-light: #ffffff;
  }
  html, body {
    margin: 0;
    padding: 0;
    width: 1200px;
    height: 1000px;
    overflow: hidden;
    background: var(--page);
  }
  .canvas {
    position: relative;
    width: 1200px;
    height: 1000px;
  }
  .card {
    position: absolute;
    left: 80px;
    top: 151px;
    width: 1039px;
    height: 697px;
    box-sizing: border-box;
    border: 2px solid var(--card-edge);
    background: var(--card);
    overflow: hidden;
  }
  .card__band {
    position: absolute;
    left: 354px;
    top: 0;
    width: 38px;
    height: 100%;
    background: var(--brand-blue);
  }
  .card__name {
    position: absolute;
    left: 26px;
    top: 278px;
    width: 310px;
    margin: 0;
    font-family: "Varela Round", sans-serif;
    font-weight: 400;
    font-size: 100px;
    line-height: 130px;
    letter-spacing: 2px;
    color: var(--brand-blue);
    white-space: nowrap;
  }
  .card__phone {
    position: absolute;
    left: 616px;
    top: 325px;
    width: 421px;
    height: 60px;
  }
  .card__phone svg {
    position: absolute;
    inset: 0;
  }
  .card__phone-number {
    position: absolute;
    left: 72px;
    top: 0;
    margin: 0;
    font-family: "Varela Round", sans-serif;
    font-size: 42px;
    line-height: 60px;
    letter-spacing: 1px;
    color: var(--text-light);
    white-space: nowrap;
  }
</style>
</head>
<body>
<main class="canvas">
  <section class="card" aria-label="KVT 3 business card, reverse side">
    <div class="card__band"></div>
    <h1 class="card__name">KVT 3</h1>
    <div class="card__phone">
      <svg width="421" height="60" viewBox="0 0 421 60" aria-hidden="true">
        <rect class="phone-tab" x="0" y="0" width="70" height="60" rx="20" fill="var(--brand-blue)"/>
        <rect class="phone-gap" x="20" y="0" width="70" height="60" rx="20" fill="var(--card)"/>
        <rect class="phone-bar" x="38" y="0" width="400" height="60" rx="20" fill="var(--brand-red)"/>
      </svg>
      <p class="card__phone-number">07945 318264</p>
    </div>
  </section>
</main>
</body>
</html>
```